Business Card Design

Business card design.

Business card is to have logo, website address and email address.

Website is www.brightkettle.ie
Email is info@brightkettle.ie
Logo uploaded

I have ordered Business Card Printing via Print Harbor, the Double-sided colour printed option with gloss finish.

Industry/Entity Type

Business

```html
<!DOCTYPE html>
<html lang="en">
<head>
<meta charset="UTF-8">
<title>Bright Kettle – Business Card</title>
<link rel="stylesheet" href="https://fonts.googleapis.com/css2?family=Nunito:wght@600;800;900&display=swap">
<style>
  :root {
    --stage: #2a2a2a;
    --paper: #ffffff;
    --paper-shade: #e4e4e4;
    --brand-red: #e0000d;
    --brand-red-deep: #b80008;
    --ink: #1c1c1c;
    --on-red: #ffffff;
    --divider: rgba(255,255,255,0.55);
  }
  * { margin: 0; padding: 0; box-sizing: border-box; }
  html, body {
    width: 1200px;
    height: 900px;
    overflow: hidden;
    background: var(--stage);
    font-family: "Nunito", "Segoe UI", sans-serif;
  }
  .sheet {
    width: 1200px;
    height: 900px;
    display: flex;
    flex-direction: column;
    align-items: center;
    justify-content: center;
    gap: 40px;
  }
  .card {
    position: relative;
    width: 700px;
    height: 400px;
    overflow: hidden;
    box-shadow: 0 12px 30px rgba(0,0,0,0.5);
  }

  /* Front */
  .card--front {
    background: radial-gradient(ellipse at 45% 45%, var(--paper) 35%, var(--paper-shade) 100%);
  }
  .card--front .corner-band {
    position: absolute;
    inset: 0;
    width: 100%;
    height: 100%;
  }
  .card--front .brand {
    position: absolute;
    left: 0;
    right: 0;
    top: 150px;
    justify-content: center;
  }
  .brand {
    display: flex;
    align-items: center;
    gap: 16px;
  }
  .brand__dot {
    width: 50px;
    height: 50px;
    border-radius: 50%;
    background: var(--brand-red);
    flex: none;
  }
  .brand__name {
    font-weight: 900;
    font-size: 58px;
    letter-spacing: 0.5px;
    color: var(--ink);
    line-height: 1;
    white-space: nowrap;
  }

  /* Back */
  .card--back {
    background: radial-gradient(ellipse at 40% 40%, var(--brand-red) 30%, var(--brand-red-deep) 100%);
    display: flex;
    align-items: center;
  }
  .card--back .brand {
    width: 410px;
    padding: 40px 36px 0 40px;
    gap: 12px;
    flex: none;
  }
  .card--back .brand__dot {
    width: 30px;
    height: 30px;
    background: var(--on-red);
  }
  .card--back .brand__name {
    color: var(--on-red);
    font-size: 28px;
  }
  .card__divider {
    width: 1px;
    height: 280px;
    background: var(--divider);
    flex: none;
  }
  .contact {
    list-style: none;
    padding-left: 34px;
    display: flex;
    flex-direction: column;
    gap: 22px;
    align-self: flex-start;
    margin-top: 70px;
  }
  .contact__item {
    display: flex;
    align-items: center;
    gap: 14px;
    color: var(--on-red);
    font-weight: 800;
    font-size: 18px;
    white-space: nowrap;
  }
  .contact__icon {
    width: 18px;
    height: 18px;
    flex: none;
  }
</style>
</head>
<body>
  <main class="sheet">
    <section class="card card--front" aria-label="Card front">
      <svg class="corner-band" viewBox="0 0 700 400" preserveAspectRatio="none" aria-hidden="true">
        <polygon points="700,300 700,400 350,400" fill="var(--brand-red)"/>
        <polygon points="700,318 700,400 400,400" fill="var(--brand-red-deep)" opacity="0.35"/>
      </svg>
      <div class="brand">
        <span class="brand__dot"></span>
        <span class="brand__name">BRIGHTKETTLE.IE</span>
      </div>
    </section>

    <section class="card card--back" aria-label="Card back">
      <div class="brand">
        <span class="brand__dot"></span>
        <span class="brand__name">BRIGHTKETTLE.IE</span>
      </div>
      <div class="card__divider"></div>
      <ul class="contact">
        <li class="contact__item">
          <svg class="contact__icon" viewBox="0 0 20 20" aria-hidden="true">
            <circle cx="10" cy="10" r="8.5" fill="none" stroke="var(--on-red)" stroke-width="1.8"/>
            <ellipse cx="10" cy="10" rx="3.8" ry="8.5" fill="none" stroke="var(--on-red)" stroke-width="1.4"/>
            <line x1="1.5" y1="10" x2="18.5" y2="10" stroke="var(--on-red)" stroke-width="1.4"/>
          </svg>
          <span>www.brightkettle.ie</span>
        </li>
        <li class="contact__item">
          <svg class="contact__icon" viewBox="0 0 20 20" aria-hidden="true">
            <rect x="1.5" y="4" width="17" height="12" fill="none" stroke="var(--on-red)" stroke-width="1.8"/>
            <polyline points="1.5,4 10,11 18.5,4" fill="none" stroke="var(--on-red)" stroke-width="1.6"/>
          </svg>
          <span>info@brightkettle.ie</span>
        </li>
      </ul>
    </section>
  </main>
</body>
</html>
```